Human Resources consulting firm website

I recently started a consulting firm after 30 years in Human Resources (Executive Development) work with Kestrel 25 companies. I am looking for a website design that will convey both the services I provide (all in the HR / executive development arena) as well as sense of trust in me and my abilities (many years of experience, breadth of knowledge).

In the attachment section, there is a document with links to a number of websites fr firms that do similar work to me - the doc shares what I like about them and what I do not. I've also include my bio to give you a sens of who I am /what I do. The head shot will be replaced soon as I'm having new photos take, but the verbiage is what's important.

I need your help with the look and feel as well as different ideas on how to share the info. I am looking for your creativity and experience. I have not done a website for anything in the past.

Looking forward to working together on a great project and product!!

Target Market(s)

Any company looking for senior leader caoching, assessments of those leaders or help with a CEO transition. My wheelhouse is Kestrel top 100 companies, but am able to work with small firms as well. Also any Board of Directors and upstarts in California.

Industry/Entity Type

Consulting

Coding

Coded - Design and coding required

Number of Pages Required

5+ page

Font styles to use
Sans Serif
Other font styles liked:
• Do not have a specific one but am very open to options

Colors

Designer to choose colors to be used in the design.

Requirements
Must have
• My project must have be professional (see the type of companies I am targeting) with an air of simplicity.
• A professional yet approachable look and feel that delivers:
• (1) I want there to be a landing page (with limited info - a more of a "teaser")
• (2) a tab for about us (with a few sentences about the company, my photo and option to link to my bio)
• (3) a tab for the services offered (one page with tiles that have a little bit about the services and the option to link to more info)
• (4) a tab to contact me (form to fill out with some personal info and the request that will get sent to my email).
• (5) diversity in the imagery
• (6) I plan for it to be mostly static. I will not be adding/changing regularly (although imagine the first couple months will want to tweak it as I get feedback). I do not plan to add blogs, etc.
Nice to have
• (1) Good graphics. I'm ok with black and white if it's classic or color photos. I don't want stalk photos anyone can get on the web. A sophisticated yet approachable look is what I'm going for.
• (2) Ability to get to know me (the principal) just a bit. That can be through the verbiage, colors, photos, etc.
• (3) Ability to contact me from the front home/landing page or contact page.
• (4) When someone looks me up on line, I want them to see a sentence or two about the company and have links that will take them straight to the page on the website they are looking for (contact, about us, etc.)
Should not have
• I do not want this to be:
• (1) overly feminine (not pink, purple, etc.),
• (2) flashy (I'm fine with a small video or moving photo but doubt I want anything beyond that) or
• (3) too close to the "out there" category (this is a professional business with corporate clients).
• (4) sterile (I'm selling myself .. that's what people buy when they hire a consultant).
• (5) basic - I do not want this to look like I hired my nephew straight out of college to build this. I'm looking for a strong, professional look.

```html
<!DOCTYPE html>
<html lang="en">
<head>
<meta charset="utf-8">
<title>Services — Harwell Talent Solutions</title>
<link rel="stylesheet" href="https://fonts.googleapis.com/css2?family=Jost:ital,wght@0,400;0,500;0,600;1,500&family=Crimson+Pro:wght@400&display=swap">
<style>
:root{
  --stage:#0f4571;
  --navy:#0d406d;
  --brand:#1a4d80;
  --steel:#7f9fc6;
  --ink:#1b1b1b;
  --paper:#ffffff;
  --mist:#f5f5f5;
  --footer:#333333;
  --footer-text:#cfcfcf;
  --quote-a:#6f9fdc;
  --quote-b:#4d83cb;
}
*{margin:0;padding:0;box-sizing:border-box}
html,body{width:1200px;height:2669px;overflow:hidden}
body{background:var(--stage);font-family:"Jost",sans-serif;color:var(--ink);position:relative}
.stage-title{position:absolute;top:80px;left:0;width:1200px;text-align:center;color:#fff;font-weight:500;font-size:25px;letter-spacing:2px}
.page{position:absolute;left:215px;top:229px;width:770px;height:2261px;background:var(--paper);overflow:hidden}

.site-header{position:absolute;top:0;left:0;width:100%;height:80px}
.brand{position:absolute;left:27px;top:17px;display:flex;align-items:center;gap:8px}
.brand-square{width:8px;height:8px;background:var(--steel)}
.brand-name{color:var(--steel);font-size:9.5px;line-height:10px;font-weight:400;text-transform:uppercase;letter-spacing:.2px}
.main-nav a{position:absolute;top:24px;font-size:8.5px;font-weight:600;letter-spacing:.6px;color:var(--ink);text-decoration:none}
.main-nav a.active{color:var(--brand);border-bottom:1.5px solid var(--brand);padding-bottom:3px}
.social-dot{position:absolute;top:25px;width:9px;height:9px;background:var(--ink);border-radius:1px}

.intro{position:absolute;left:49px;top:118px}
.intro h1{font-family:"Crimson Pro",serif;font-weight:400;font-size:35px;color:var(--brand)}
.intro p{font-size:17.5px;line-height:30px;margin-top:20px;color:var(--ink)}

.hero-photo{position:absolute;left:0;top:299px;width:770px;height:308px;
  background:linear-gradient(100deg,#cfc6ba 0%,#8d8a86 30%,#dcd6cd 55%,#efe9e1 80%,#c9b89f 100%)}

.services{position:absolute;left:0;top:607px;width:770px;height:945px;background:var(--mist)}
.services-lead{position:absolute;left:167px;top:54px;width:436px;text-align:center;font-size:11px;line-height:19px;font-weight:500}
.service-card{position:absolute;left:34px;top:159px;width:700px;height:745px;background:var(--paper)}
.service{position:absolute;width:285px}
.service svg{position:absolute;left:0;top:0}
.service h3{position:absolute;top:75px;font-size:9px;font-weight:600;letter-spacing:1px;color:var(--brand)}
.service p{position:absolute;top:95px;width:285px;font-size:11px;line-height:18.7px;font-weight:500}

.testimonial{position:absolute;left:33px;top:1597px;width:705px;height:319px}
.testimonial-photo{position:absolute;inset:0;background:linear-gradient(110deg,var(--quote-b) 0%,var(--quote-a) 45%,#8bb3e4 60%,var(--quote-b) 100%)}
.testimonial-frame{position:absolute;left:19px;top:19px;right:19px;bottom:19px;border:1px solid rgba(255,255,255,.75)}
.quote-mark{position:absolute;top:50px;width:100%;text-align:center;color:#fff;font-family:"Crimson Pro",serif;font-size:46px;line-height:40px}
.quote-text{position:absolute;top:122px;left:80px;width:545px;text-align:center;color:#fff;font-size:13.5px;line-height:24px}
.quote-cite{position:absolute;top:226px;width:100%;text-align:center;color:#fff;font-size:8.5px;font-weight:500;letter-spacing:.5px;line-height:17px}
.quote-cite em{font-style:italic}

.contact-band{position:absolute;left:31px;top:1974px;width:705px;height:117px;background:var(--navy);z-index:2;color:#fff}
.contact-band .label{position:absolute;left:32px;top:33px;font-size:8.5px;font-weight:600;letter-spacing:1px}
.contact-band .headline{position:absolute;left:32px;top:52px;font-size:16px}
.contact-band .cta{position:absolute;left:511px;top:38px;width:156px;height:42px;border:2px solid #fff;font-size:10px;font-weight:600;letter-spacing:1.3px;display:flex;align-items:center;justify-content:center}

.site-footer{position:absolute;left:0;top:2072px;width:770px;height:189px;background:var(--footer);color:var(--footer-text)}
.footer-brand{position:absolute;left:43px;top:77px;display:flex;align-items:center;gap:8px}
.footer-brand .brand-name{color:#fff}
.footer-brand .brand-square{background:#fff}
.footer-col{position:absolute;top:76px;font-size:8.5px;line-height:17.5px;letter-spacing:.4px}
.footer-col.pages{left:377px}
.footer-col.social{left:462px}
.footer-col.info{left:569px;text-transform:none}
.mini-dot{display:inline-block;width:6px;height:6px;background:var(--footer-text);margin-right:5px;vertical-align:0}
</style>
</head>
<body>
<div class="stage-title">SERVICES PAGE</div>

<main class="page">
  <header class="site-header">
    <div class="brand"><span class="brand-square"></span><span class="brand-name">Harwell<br>Talent<br>Solutions</span></div>
    <nav class="main-nav">
      <a href="#" style="left:510px">ABOUT</a>
      <a href="#" class="active" style="left:565px">SERVICES</a>
      <a href="#" style="left:630px">CONTACT</a>
    </nav>
    <span class="social-dot" style="left:708px"></span>
    <span class="social-dot" style="left:731px;border-radius:50%"></span>
  </header>

  <section class="intro">
    <h1>Services</h1>
    <p>Short description about what Harwell Talent Solution services.<br>Lorem ipsum dolor sit amet, consectetur adipiscing elit.</p>
  </section>

  <div class="hero-photo" role="img" aria-label="Photo of a person typing on a laptop at a bright desk"></div>

  <section class="services">
    <p class="services-lead">Further information about all services offered. Lorem ipsum dolor sit amet, consectetur adipiscing elit, sed do eiusmod tempor incididunt ut labore et dolore magna aliqua. Ut enim ad minim veniam, quis nostrud exercitation ullamco laboris nisi.</p>

    <div class="service-card">
      <div class="service" style="left:51px;top:54px">
        <svg width="70" height="50" viewBox="0 0 70 50" fill="none" stroke="#1a4d80" stroke-width="3">
          <rect x="26" y="2" width="18" height="12" rx="1"/><path d="M32 14l-3 5 7-5"/>
          <circle cx="10" cy="18" r="4"/><circle cx="60" cy="18" r="4"/>
          <path d="M4 48V28h10v12h8V26h26v14h8V28h10v20"/><path d="M35 26v22"/>
        </svg>
        <h3>SERVICE #1</h3>
        <p>Short paragraph of Service. Labore et dolore magna aliqua. Ut enim ad minim veniam, quis nostrud exer-citation ullamco laboris nisi quis nostrud exercitation ullamco laboris nisi.</p>
      </div>
      <div class="service" style="left:371px;top:54px">
        <svg width="72" height="50" viewBox="0 0 72 50">
          <path d="M3 46L42 14l8 6L68 4" fill="none" stroke="#1a4d80" stroke-width="3"/>
          <path d="M61 2h9v9" fill="none" stroke="#1a4d80" stroke-width="3"/>
          <g fill="#1a4d80"><rect x="26" y="36" width="6" height="12"/><rect x="35" y="30" width="6" height="18"/><rect x="44" y="28" width="6" height="20"/><rect x="53" y="20" width="6" height="28"/><rect x="62" y="14" width="6" height="34"/></g>
        </svg>
        <h3>SERVICE #2</h3>
        <p>Short paragraph of Service. Labore et dolore magna aliqua. Ut enim ad minim veniam, quis nostrud exer-citation ullamco laboris nisi quis nostrud exercitation ullamco laboris nisi.</p>
      </div>
      <div class="service" style="left:51px;top:271px">
        <svg width="50" height="62" viewBox="0 0 50 62" fill="none" stroke="#1a4d80" stroke-width="2.5">
          <path d="M2 2h34l10 10v48H2z"/><path d="M36 2v10h10"/>
          <path d="M10 22h28M10 29h28M10 36h28M10 43h28M10 50h28M24 15h12" stroke-width="1.5"/>
        </svg>
        <h3>SERVICE #3</h3>
        <p>Short paragraph of Service. Labore et dolore magna aliqua. Ut enim ad minim veniam, quis nostrud exer-citation ullamco laboris nisi quis nostrud exercitation ullamco laboris nisi.</p>
      </div>
      <div class="service" style="left:371px;top:271px">
        <svg width="64" height="64" viewBox="0 0 64 64">
          <path d="M28 6A27 27 0 1 0 58 36H28z" fill="none" stroke="#1a4d80" stroke-width="2.5"/>
          <path d="M22 10A22 22 0 0 0 24 52" fill="none" stroke="#1a4d80" stroke-width="2"/>
          <path d="M34 2a28 28 0 0 1 28 28H34z" fill="none" stroke="#1a4d80" stroke-width="2.5"/>
          <path d="M34 2l14 28M34 30l24-14" stroke="#1a4d80" stroke-width="2"/>
          <path d="M32 36h26A26 26 0 0 1 32 62z" fill="#1a4d80"/>
        </svg>
        <h3>SERVICE #4</h3>
        <p>Short paragraph of Service. Labore et dolore magna aliqua. Ut enim ad minim veniam, quis nostrud exer-citation ullamco laboris nisi quis nostrud exercitation ullamco laboris nisi.</p>
      </div>
      <div class="service" style="left:41px;top:488px">
        <svg width="56" height="66" viewBox="0 0 56 66" fill="none" stroke="#1a4d80" stroke-width="2.5">
          <path d="M28 12a15 15 0 0 0-9 27v8h18v-8a15 15 0 0 0-9-27z"/>
          <path d="M21 51h14M22 55h12M25 59h6M24 40v-8h8v8M28 32v8"/>
          <path d="M28 2v5M12 7l3 4M44 7l-3 4M4 20l5 2M52 20l-5 2M3 34h5M48 34h5" stroke-width="1.5"/>
        </svg>
        <h3 style="left:10px">SERVICE #5</h3>
        <p style="left:10px">Short paragraph of Service. Labore et dolore magna aliqua. Ut enim ad minim veniam, quis nostrud exer-citation ullamco laboris nisi quis nostrud exercitation ullamco laboris nisi.</p>
      </div>
      <div class="service" style="left:371px;top:488px">
        <svg width="72" height="56" viewBox="0 0 72 56" fill="none" stroke="#1a4d80" stroke-width="2.5">
          <rect x="2" y="2" width="67" height="52"/>
          <path d="M14 14l3 3 6-7" stroke-width="2"/>
          <rect x="13" y="24" width="7" height="7" stroke-width="1.8"/><rect x="13" y="37" width="7" height="7" stroke-width="1.8"/>
          <path d="M28 14h30M28 20h24M28 27h30M28 33h24M28 40h30M28 46h24" stroke-width="1.6"/>
        </svg>
        <h3>SERVICE #6</h3>
        <p>Short paragraph of Service. Labore et dolore magna aliqua. Ut enim ad minim veniam, quis nostrud exer-citation ullamco laboris nisi quis nostrud exercitation ullamco laboris nisi.</p>
      </div>
    </div>
  </section>

  <section class="testimonial">
    <div class="testimonial-photo" role="img" aria-label="Blue-toned photo of two colleagues talking at an office desk"></div>
    <div class="testimonial-frame"></div>
    <div class="quote-mark">&ldquo;</div>
    <p class="quote-text">Testimonial from client goes here. Testimonial from client goes here. Testimonial from client goes here. Testimonial from client goes here. Testimonial from client goes here. Testimonial from client goes here. Testimonial from client goes here.</p>
    <p class="quote-cite">NAME OF CLIENT &nbsp;|&nbsp; <em>TITLE OF CLIENT</em><br>COMPANY NAME</p>
  </section>

  <section class="contact-band">
    <span class="label">CONTACT US</span>
    <span class="headline">We would love to collaborate with you</span>
    <a class="cta">GET IN TOUCH</a>
  </section>

  <footer class="site-footer">
    <div class="footer-brand"><span class="brand-square"></span><span class="brand-name">Harwell<br>Talent<br>Solutions</span></div>
    <div class="footer-col pages">Home<br>About<br>Services<br>Contact</div>
    <div class="footer-col social"><span class="mini-dot"></span>Profile<br><span class="mini-dot" style="border-radius:50%"></span>Social</div>
    <div class="footer-col info">HARWELL TALENT SOLUTIONS<br>name@domain-name.com<br>123.456.7890</div>
  </footer>
</main>
</body>
</html>
```